Design for "Vellow" protein health bars wrappers

I need a new design for a protein bar that my partners and I are launching for the North American and European markets.
The bar's name is "Vellow."
Given the masculine/aggressive nature of that name, we are thinking of neutralizing it with a more feminine/soft font and design. But hey - the sky is the limit. We obviously want this 20-gram protein bar to sell to a wide net (not just men but women also). So if it means having a Pellam Comic font/design (or whatever) in order to do this, so be it. I leave it up to your intelligence and experience.

ADDED ON FEBRUARY 24:

The official name of the bar is just "VELLOW" (not "Vellow Protein").

We have six flavors divided into two categories, which are 1) SOFT and 2) CRUNCHY.
So, the idea is to make two similar designs for the wrapper that still distinguish themselves from each other because one is 'soft' and the other is 'crunchy.'
Then, within each category, the idea is to have three color variations, designating the three flavors in each category.

Please look at the dimensions and examples of the generic wrapper designs that we already have (and which we find too generic), which I have uploaded.

Target Market(s)

North America - Brindle, Fair Harvest
Europe - Norway, Sweden, Denmark, Germany, France, Switzerland, Italy.

Industry/Entity Type

Nutrition

Logo Text

Vellow

Font styles to use
Serif
Decorative

Colors
fff6dc
f04a50

Requirements
Must have
• The title is "Vellow".
• We have six flavors divided into two categories, which are 1) SOFT and 2) CRUNCHY.
• You can work on the two different types of similar-but-different designs for the "soft" and for the "cruncy." Then it's just a question of color variations for each flavor.
• The flavors are:
• SOFT: 1) strawberry, 2) Chocolate brownie, 3) Cinnamon Crunch
• CRUNCY: 1) Peanut, 2) Lemon, 3) Coconut.
• On the side or at the bottom, there should be stated:
• "20 gm protein"
• "children friendly"
Nice to have
• Obvious: a design that catches the eye and inspires someone to buy the bar to eat it.
• Part of the design could include a photograph of the actual bar (you can use generic photos for that until we place a pic of the actual bar). Like 1/4th of the total surface (or even a little smaller).

```html
<!DOCTYPE html>
<html lang="en">
<head>
<meta charset="utf-8">
<title>Vellow Protein Bar Wrappers</title>
<link rel="stylesheet" href="https://fonts.googleapis.com/css2?family=Anton&family=Oswald:wght@500;700&family=Kalam:wght@700&display=swap">
<style>
  :root {
    --bg: #e4ebef;
    --wrapper: #0d0d0d;
    --speckle: #3a3a3a;
    --crimp: #2a2a2a;
    --white: #ffffff;
    --ink: #111111;
    --peanut: #b5002a;
    --peanut-photo-a: #e9b26a;
    --peanut-photo-b: #b97a3a;
    --lemon: #2e6b1c;
    --lemon-accent: #f5c518;
    --lemon-photo-a: #ffe36a;
    --lemon-photo-b: #f0b400;
    --coconut: #6b4a36;
    --coconut-accent: #2f7d1e;
    --coconut-photo-a: #f4f1ea;
    --coconut-photo-b: #7a5a40;
  }
  * { margin: 0; padding: 0; box-sizing: border-box; }
  html, body { width: 1200px; height: 840px; overflow: hidden; }
  body { background: var(--bg); font-family: "Oswald", sans-serif; position: relative; }

  .wrapper { position: absolute; }
  .wrapper-shape { position: absolute; inset: 0; width: 100%; height: 100%; }
  .wrapper-body { fill: var(--wrapper); }
  .crimp-line { stroke: var(--crimp); stroke-width: 0.4; }

  .texture {
    position: absolute; left: 4%; right: 4%; top: 0; bottom: 0;
    background:
      radial-gradient(ellipse at 30% 25%, rgba(90,90,90,.35), transparent 55%),
      radial-gradient(ellipse at 75% 70%, rgba(90,90,90,.28), transparent 50%);
  }

  .wrapper--peanut  { left: 70px;  top: 50px;  width: 740px; height: 290px; }
  .wrapper--lemon   { left: 560px; top: 350px; width: 590px; height: 270px; }
  .wrapper--coconut { left: 40px;  top: 510px; width: 530px; height: 260px; }

  .photo-peanut-a  { stop-color: var(--peanut-photo-a); }
  .photo-peanut-b  { stop-color: var(--peanut-photo-b); }
  .photo-lemon-a   { stop-color: var(--lemon-photo-a); }
  .photo-lemon-b   { stop-color: var(--lemon-photo-b); }
  .photo-coconut-a { stop-color: var(--coconut-photo-a); }
  .photo-coconut-b { stop-color: var(--coconut-photo-b); }

  .flame { position: absolute; }
  .flame--peanut  { fill: var(--peanut); }
  .flame--lemon   { fill: var(--lemon-accent); }
  .flame--coconut { fill: var(--coconut-accent); }

  .badges { position: absolute; display: flex; gap: 3px; }
  .badge {
    width: 44px; height: 44px; border-radius: 50%;
    background: var(--white); border: 2px solid var(--wrapper);
    outline: 2px solid var(--white);
    display: flex; flex-direction: column; align-items: center; justify-content: center;
    color: var(--ink); text-align: center; line-height: 1;
  }
  .badge-label { font-size: 7px; font-weight: 500; color: var(--ink); }
  .badge-value { font-size: 12px; font-weight: 700; margin-top: 2px; color: var(--ink); }
  .badge-heart { width: 12px; height: 11px; margin-bottom: 1px; }

  .flavor-pill {
    position: absolute; background: var(--white); border-radius: 30px;
    font-family: "Kalam", cursive; font-weight: 700;
    display: flex; align-items: center; justify-content: center;
  }

  .wordmark {
    position: absolute; color: var(--white);
    font-family: "Anton", sans-serif; font-weight: 400;
    line-height: 1; letter-spacing: 1px; text-transform: uppercase;
  }

  .wrapper--peanut .badges { left: 92px; top: 96px; }
  .wrapper--peanut .flavor-pill { left: 212px; top: 86px; width: 180px; height: 50px; font-size: 32px; color: var(--peanut); }
  .wrapper--peanut .flame { left: 110px; top: 150px; width: 150px; height: 120px; }
  .wrapper--peanut .wordmark { left: 212px; top: 132px; font-size: 140px; }

  .wrapper--lemon .badges { left: 60px; top: 70px; }
  .wrapper--lemon .flavor-pill { left: 166px; top: 58px; width: 150px; height: 44px; font-size: 26px; color: var(--lemon); }
  .wrapper--lemon .flame { left: 70px; top: 138px; width: 120px; height: 105px; }
  .wrapper--lemon .wordmark { left: 166px; top: 108px; font-size: 122px; }

  .wrapper--coconut .badges { left: 52px; top: 62px; }
  .wrapper--coconut .badge { width: 40px; height: 40px; }
  .wrapper--coconut .flavor-pill { left: 150px; top: 58px; width: 150px; height: 40px; font-size: 24px; color: var(--peanut); }
  .wrapper--coconut .flame { left: 50px; top: 128px; width: 120px; height: 100px; }
  .wrapper--coconut .wordmark { left: 150px; top: 104px; font-size: 110px; }
</style>
</head>
<body>

<svg width="0" height="0" style="position:absolute">
  <defs>
    <linearGradient id="photo-peanut" x1="0" y1="0" x2="1" y2="1">
      <stop offset="0" class="photo-peanut-a"/><stop offset="1" class="photo-peanut-b"/>
    </linearGradient>
    <linearGradient id="photo-lemon" x1="0" y1="0" x2="1" y2="1">
      <stop offset="0" class="photo-lemon-a"/><stop offset="1" class="photo-lemon-b"/>
    </linearGradient>
    <linearGradient id="photo-coconut" x1="0" y1="0" x2="1" y2="0">
      <stop offset="0" class="photo-coconut-a"/><stop offset="1" class="photo-coconut-b"/>
    </linearGradient>
    <symbol id="heart" viewBox="0 0 24 22">
      <path d="M12 21 C4 14 0 10 0 6 A6 6 0 0 1 12 4 A6 6 0 0 1 24 6 C24 10 20 14 12 21Z" fill="#111111"/>
    </symbol>
    <symbol id="wrapper-outline" viewBox="0 0 100 100" preserveAspectRatio="none">
      <polygon class="wrapper-body" points="2.5,0 0,6.25 2.5,12.5 0,18.75 2.5,25 0,31.25 2.5,37.5 0,43.75 2.5,50 0,56.25 2.5,62.5 0,68.75 2.5,75 0,81.25 2.5,87.5 0,93.75 2.5,100 97.5,100 100,93.75 97.5,87.5 100,81.25 97.5,75 100,68.75 97.5,62.5 100,56.25 97.5,50 100,43.75 97.5,37.5 100,31.25 97.5,25 100,18.75 97.5,12.5 100,6.25 97.5,0"/>
    </symbol>
  </defs>
</svg>

<article class="wrapper wrapper--peanut">
  <svg class="wrapper-shape" viewBox="0 0 100 100" preserveAspectRatio="none">
    <use href="#wrapper-outline" width="100" height="100"/>
    <polygon role="img" aria-label="Photo of roasted peanuts" fill="url(#photo-peanut)" points="42,100 44,90 50,86 56,84 62,80 70,78 76,74 84,72 90,68 96,66 96,100"/>
    <line class="crimp-line" x1="5" y1="0" x2="5" y2="100"/>
    <line class="crimp-line" x1="95" y1="0" x2="95" y2="100"/>
  </svg>
  <div class="texture" role="img" aria-label="Grey speckled texture"></div>
  <svg class="flame flame--peanut" viewBox="0 0 100 100" preserveAspectRatio="none" role="img" aria-label="Flame graphic in peanut red">
    <polygon points="10,0 100,0 100,100 10,100 30,50"/>
  </svg>
  <div class="badges">
    <div class="badge"><span class="badge-label">PROTEIN</span><span class="badge-value">20 gr</span></div>
    <div class="badge"><svg class="badge-heart"><use href="#heart"/></svg><span class="badge-label">CHILDREN<br>FRIENDLY</span></div>
  </div>
  <div class="flavor-pill">Peanut</div>
  <h2 class="wordmark">Vellow</h2>
</article>

<article class="wrapper wrapper--lemon">
  <svg class="wrapper-shape" viewBox="0 0 100 100" preserveAspectRatio="none">
    <use href="#wrapper-outline" width="100" height="100"/>
    <polygon role="img" aria-label="Photo of sliced lemons" fill="url(#photo-lemon)" points="38,100 40,90 52,86 64,84 74,80 84,76 92,72 96,70 96,100"/>
    <line class="crimp-line" x1="5" y1="0" x2="5" y2="100"/>
    <line class="crimp-line" x1="95" y1="0" x2="95" y2="100"/>
  </svg>
  <div class="texture" role="img" aria-label="Grey speckled texture"></div>
  <svg class="flame flame--lemon" viewBox="0 0 100 100" preserveAspectRatio="none" role="img" aria-label="Flame graphic in lemon yellow">
    <polygon points="10,0 100,0 100,100 10,100 30,50"/>
  </svg>
  <div class="badges">
    <div class="badge"><span class="badge-label">PROTEIN</span><span class="badge-value">20 gr</span></div>
    <div class="badge"><svg class="badge-heart"><use href="#heart"/></svg><span class="badge-label">CHILDREN<br>FRIENDLY</span></div>
  </div>
  <div class="flavor-pill">Lemon</div>
  <h2 class="wordmark">Vellow</h2>
</article>

<article class="wrapper wrapper--coconut">
  <svg class="wrapper-shape" viewBox="0 0 100 100" preserveAspectRatio="none">
    <use href="#wrapper-outline" width="100" height="100"/>
    <polygon role="img" aria-label="Photo of a split coconut" fill="url(#photo-coconut)" points="20,100 22,92 40,90 60,88 78,86 96,84 96,100"/>
    <line class="crimp-line" x1="5" y1="0" x2="5" y2="100"/>
    <line class="crimp-line" x1="95" y1="0" x2="95" y2="100"/>
  </svg>
  <div class="texture" role="img" aria-label="Grey speckled texture"></div>
  <svg class="flame flame--coconut" viewBox="0 0 100 100" preserveAspectRatio="none" role="img" aria-label="Flame graphic in coconut green">
    <polygon points="10,0 100,0 100,100 10,100 30,50"/>
  </svg>
  <div class="badges">
    <div class="badge"><span class="badge-label">PROTEIN</span><span class="badge-value">20 gr</span></div>
    <div class="badge"><svg class="badge-heart"><use href="#heart"/></svg><span class="badge-label">CHILDREN<br>FRIENDLY</span></div>
  </div>
  <div class="flavor-pill">Coconut</div>
  <h2 class="wordmark">Vellow</h2>
</article>

</body>
</html>
```